Valtrix Inc

Hello.

I would like to take a wordpress ecomm template and turn it into a website that can display 100s of domain listings with short text box for description and a price .
One link to quibblepay.example for immediate payment and with the confirmation/decline letter/email .
Five - six pages, Home, about us, domains, contact us, . Several columns or scrolling page for the domain page. I want to list several hundred virtual domains for sale .
Like a portfolio website but lists domain text .
This will be hosted on my server. On my domain.

Target Market(s)

End users, business owners, store front managers, online entpenauers , ect

Industry/Entity Type

Information Technology

Number of Pages Required

5+ page

Font styles to use
Sans Serif

Colors
0455a3
f78f20
abd036

Requirements
Must have
• Lots of white space, clean professional look . fast loading , use of greens and blues. Easy to read font.
• big headers , several - three different headers that rotate or move or clicks.
• A few current stock photos.
Should not have
• slow loading photos.
• More than two photos on any one page.

```html
<!DOCTYPE html>
<html lang="en">
<head>
<meta charset="utf-8">
<title>Valtrix Inc — Domains for Sale</title>
<link href="https://fonts.googleapis.com/css2?family=Open+Sans:wght@400;600;700&family=Roboto+Condensed:wght@700&family=Source+Sans+3:wght@400;600;700&display=swap" rel="stylesheet">
<style>
:root{
  --blue:#0455a3;
  --blue-dark:#034584;
  --orange:#f78f20;
  --frame:#e4e4e4;
  --ink:#222;
  --row-alt:#eeeeee;
  --rule:#d2d2d2;
  --footer:#1c1c1c;
  --field:#3a3a3a;
  --muted:#8a8a8a;
}
*{box-sizing:border-box;margin:0;padding:0}
html,body{width:694px;height:1200px;overflow:hidden}
body{background:var(--frame);font-family:"Open Sans",sans-serif;color:var(--ink);position:relative}
.page{position:absolute;left:8px;top:8px;width:678px;height:1184px;background:#fff;overflow:hidden}

/* header */
.hero{position:absolute;left:0;top:0;width:678px;height:261px;
  background:radial-gradient(ellipse at 55% 35%,#6b6b6b 0%,#3d3d3d 45%,#151515 100%)}
.hero-photo{position:absolute;inset:0}
.contact-bar{position:absolute;right:0;top:0;width:318px;height:26px;background:var(--blue);
  clip-path:polygon(0 0,100% 0,100% 100%,18px 100%);display:flex;align-items:center;gap:14px;padding-left:34px;
  color:#fff;font-family:"Source Sans 3",sans-serif;font-weight:700;font-size:10px}
.contact-bar span{display:flex;align-items:center;gap:5px}
.social{display:flex;gap:3px}
.social i{width:11px;height:11px;border:1.2px solid #fff;border-radius:50%;display:block}
.logo{position:absolute;left:20px;top:20px;font-family:"Open Sans",sans-serif;font-weight:700;font-size:31px;color:var(--orange);letter-spacing:-.5px}
.nav{position:absolute;right:18px;top:50px;display:flex;align-items:center;gap:12px;
  font-family:"Roboto Condensed",sans-serif;font-weight:700;font-size:10px;color:#fff}
.nav a{color:#fff;text-decoration:none}
.nav .current{color:var(--orange);border-bottom:2px solid var(--orange);padding-bottom:2px}
.nav .cta{background:var(--blue);padding:5px 8px;border-radius:2px}
.search{position:absolute;left:165px;top:194px;width:348px;height:30px;border:1.5px solid #fff;border-radius:3px;
  display:flex;overflow:hidden;background:rgba(70,70,70,.85)}
.search-field{flex:1;display:flex;align-items:center;gap:9px;padding-left:8px;color:#ddd;font-weight:700;font-size:14px}
.search-btn{width:63px;background:var(--blue);color:#fff;font-family:"Source Sans 3",sans-serif;font-weight:700;font-size:9.5px;display:flex;align-items:center;justify-content:center}

/* listing */
.title{position:absolute;left:0;top:294px;width:678px;text-align:center;font-size:19px;font-weight:400;color:var(--orange)}
.title strong{color:var(--blue);font-weight:700}
.listing{position:absolute;left:38px;top:342px;width:601px;height:620px;border:1px solid var(--rule)}
table{border-collapse:collapse;width:585px;table-layout:fixed;font-family:"Source Sans 3",sans-serif;font-size:9px;font-weight:600}
th{height:29px;background:linear-gradient(#e6e6e6,#d6d6d6);color:var(--blue);font-size:9.5px;font-weight:700;border-right:1px solid #c8c8c8}
th .h{display:inline-flex;align-items:center;gap:6px}
td{height:17.35px;border-right:1px solid var(--rule);border-top:1px solid #dcdcdc;white-space:nowrap;overflow:hidden;padding:0 6px}
tbody tr:nth-child(even){background:var(--row-alt)}
td.name{padding-left:12px}
td.price,td.pay{text-align:center}
.pay-mark{display:inline-block;width:6px;height:7px;background:var(--blue);vertical-align:middle}
.pay-head{font-style:normal;font-weight:700;color:var(--blue);font-size:10px}
.scroll{position:absolute;right:0;top:29px;width:16px;height:590px;background:#f2f2f2;border-left:1px solid var(--rule)}
.scroll .thumb{position:absolute;left:3px;top:14px;width:9px;height:152px;border:1px solid #bbb;border-radius:5px;background:#fafafa}
.scroll svg{position:absolute;left:3px}

/* footer */
.footer{position:absolute;left:0;top:994px;width:678px;height:168px;background:var(--footer)}
.footer-logo{position:absolute;left:34px;top:70px;font-weight:700;font-size:28px;color:var(--orange);letter-spacing:-.5px}
.about{position:absolute;left:242px;top:26px;width:160px}
.footer h3{color:#fff;font-size:9.5px;font-weight:700;margin-bottom:9px}
.about p{color:var(--muted);font-size:7.3px;line-height:10px}
.contact{position:absolute;left:465px;top:26px;width:178px}
.field{background:var(--field);color:#999;font-size:6.5px;padding:4px 8px;height:16px;margin-bottom:4px;border-radius:1px}
.field.msg{height:39px}
.submit{display:inline-block;margin-top:4px;background:#3a3a3a;color:#fff;font-size:8px;font-weight:700;padding:3px 18px;border-radius:1px;border:1px solid #555}
.copy{position:absolute;left:0;top:1162px;width:678px;height:22px;background:var(--blue);color:#fff;
  font-size:6.3px;font-weight:700;display:flex;align-items:center;justify-content:space-between;padding:0 22px 0 19px}
.copy .social i{width:11px;height:11px;background:#fff;border:none}
</style>
</head>
<body>
<div class="page">
  <header class="hero">
    <div class="hero-photo" role="img" aria-label="Blurred close-up of a web address being handwritten with a marker"></div>
    <div class="contact-bar">
      <span><svg width="11" height="11" viewBox="0 0 12 12"><path d="M3 1l2 2.5-1.2 1.3a7 7 0 0 0 3.4 3.4L8.5 7 11 9l-1 2C5 11 1 7 1 2z" fill="none" stroke="#fff" stroke-width="1.2"/></svg>1-800-555-0142</span>
      <span><svg width="12" height="12" viewBox="0 0 12 12"><circle cx="6" cy="6" r="5.3" fill="none" stroke="#fff"/><rect x="3" y="4" width="6" height="4" fill="none" stroke="#fff" stroke-width=".9"/><path d="M3 4l3 2.2L9 4" fill="none" stroke="#fff" stroke-width=".9"/></svg>info@valtrix.example</span>
      <span class="social"><i></i><i></i><i></i></span>
    </div>
    <div class="logo">VALTRIX</div>
    <nav class="nav">
      <a class="current" href="#">HOME</a>
      <a href="#">ABOUT US</a>
      <a href="#">DOMAINS</a>
      <a href="#">CONTACT</a>
      <a class="cta" href="#">SEARCH DOMAIN</a>
    </nav>
    <div class="search">
      <div class="search-field"><svg width="18" height="18" viewBox="0 0 18 18"><circle cx="7" cy="7" r="5.5" fill="none" stroke="#ddd" stroke-width="2"/><path d="M11 11l5.5 5.5" stroke="#ddd" stroke-width="2.4"/></svg>www.</div>
      <div class="search-btn">SEARCH</div>
    </div>
  </header>

  <h2 class="title">DOMAINS <strong>FOR SALE</strong></h2>

  <section class="listing">
    <table>
      <colgroup><col style="width:174px"><col style="width:266px"><col style="width:70px"><col style="width:75px"></colgroup>
      <thead>
        <tr>
          <th><span class="h"><svg width="12" height="12" viewBox="0 0 12 12"><circle cx="6" cy="6" r="5.5" fill="var(--orange)"/><path d="M1 6h10M6 .5c-2.5 3-2.5 8 0 11M6 .5c2.5 3 2.5 8 0 11" fill="none" stroke="#fff" stroke-width=".8"/></svg>DOMAIN NAME</span></th>
          <th><span class="h"><svg width="13" height="12" viewBox="0 0 13 12"><rect x=".5" y=".5" width="12" height="11" fill="none" stroke="var(--orange)"/><path d="M3 4h7M3 6h7M3 8h5" stroke="var(--orange)"/></svg>DESCRIPTIONS</span></th>
          <th><span class="h"><svg width="9" height="12" viewBox="0 0 9 12"><path d="M0 0h9v9l-4.5 3L0 9z" fill="var(--orange)"/></svg>PRICE</span></th>
          <th><span class="pay-head">QuibblePay</span></th>
        </tr>
      </thead>
      <tbody>
        <tr><td class="name">abc.example</td><td>Lorem ipsum dolor sit amet, consectetuer adipiscing elit sed diam.</td><td class="price">$2.99</td><td class="pay"><i class="pay-mark"></i></td></tr>
        <tr><td class="name">abca.example</td><td>Ut wisi enim ad minim veniam, quis nostrud exerci tation.</td><td class="price">$3.99</td><td class="pay"><i class="pay-mark"></i></td></tr>
        <tr><td class="name">abccorp.example</td><td>Nam liber tempor cum soluta nobis eleifend option congue nihil.</td><td class="price">$2.99</td><td class="pay"><i class="pay-mark"></i></td></tr>
        <tr><td class="name">abccompany.example</td><td>Typi non habent claritatem insitam; est usus legentis.</td><td class="price">$2.99</td><td class="pay"><i class="pay-mark"></i></td></tr>
        <tr><td class="name">acquil.example</td><td>Claritas est etiam processus dynamicus, qui sequitur mutationem.</td><td class="price">$4.99</td><td class="pay"><i class="pay-mark"></i></td></tr>
        <tr><td class="name">acquile.example</td><td>Lorem ipsum dolor sit amet, consectetuer adipiscing elit sed diam.</td><td class="price">$5.99</td><td class="pay"><i class="pay-mark"></i></td></tr>
        <tr><td class="name">acquire.example</td><td>Ut wisi enim ad minim veniam, quis nostrud exerci tation.</td><td class="price">$6.99</td><td class="pay"><i class="pay-mark"></i></td></tr>
        <tr><td class="name">acknowledge.example</td><td>Nam liber tempor cum soluta nobis eleifend option congue nihil.</td><td class="price">$7.99</td><td class="pay"><i class="pay-mark"></i></td></tr>
        <tr><td class="name">act.example</td><td>Typi non habent claritatem insitam; est usus legentis.</td><td class="price">$5.99</td><td class="pay"><i class="pay-mark"></i></td></tr>
        <tr><td class="name">actcorp.example</td><td>Claritas est etiam processus dynamicus, qui sequitur mutationem.</td><td class="price">$2.99</td><td class="pay"><i class="pay-mark"></i></td></tr>
        <tr><td class="name">actcorporation.example</td><td>Lorem ipsum dolor sit amet, consectetuer adipiscing elit sed diam.</td><td class="price">$3.99</td><td class="pay"><i class="pay-mark"></i></td></tr>
        <tr><td class="name">actingcorp.example</td><td>Ut wisi enim ad minim veniam, quis nostrud exerci tation.</td><td class="price">$2.99</td><td class="pay"><i class="pay-mark"></i></td></tr>
        <tr><td class="name">admissions.example</td><td>Nam liber tempor cum soluta nobis eleifend option congue nihil.</td><td class="price">$3.99</td><td class="pay"><i class="pay-mark"></i></td></tr>
        <tr><td class="name">autoart.example</td><td>Typi non habent claritatem insitam; est usus legentis.</td><td class="price">$2.99</td><td class="pay"><i class="pay-mark"></i></td></tr>
        <tr><td class="name">autocare.example</td><td>Claritas est etiam processus dynamicus, qui sequitur mutationem.</td><td class="price">$2.99</td><td class="pay"><i class="pay-mark"></i></td></tr>
        <tr><td class="name">autodealers.example</td><td>Lorem ipsum dolor sit amet, consectetuer adipiscing elit sed diam.</td><td class="price">$4.99</td><td class="pay"><i class="pay-mark"></i></td></tr>
        <tr><td class="name">autodetails.example</td><td>Ut wisi enim ad minim veniam, quis nostrud exerci tation.</td><td class="price">$5.99</td><td class="pay"><i class="pay-mark"></i></td></tr>
        <tr><td class="name">autonewyork.example</td><td>Nam liber tempor cum soluta nobis eleifend option congue nihil.</td><td class="price">$6.99</td><td class="pay"><i class="pay-mark"></i></td></tr>
        <tr><td class="name">autony.example</td><td>Typi non habent claritatem insitam; est usus legentis.</td><td class="price">$7.99</td><td class="pay"><i class="pay-mark"></i></td></tr>
        <tr><td class="name">autonj.example</td><td>Claritas est etiam processus dynamicus, qui sequitur mutationem.</td><td class="price">$5.99</td><td class="pay"><i class="pay-mark"></i></td></tr>
        <tr><td class="name">autoshine.example</td><td>Lorem ipsum dolor sit amet, consectetuer adipiscing elit sed diam.</td><td class="price">$2.99</td><td class="pay"><i class="pay-mark"></i></td></tr>
        <tr><td class="name">benn.example</td><td>Ut wisi enim ad minim veniam, quis nostrud exerci tation.</td><td class="price">$3.99</td><td class="pay"><i class="pay-mark"></i></td></tr>
        <tr><td class="name">borgauto.example</td><td>Nam liber tempor cum soluta nobis eleifend option congue nihil.</td><td class="price">$2.99</td><td class="pay"><i class="pay-mark"></i></td></tr>
        <tr><td class="name">bridesandgroomnewyork.example</td><td>Typi non habent claritatem insitam; est usus legentis.</td><td class="price">$3.99</td><td class="pay"><i class="pay-mark"></i></td></tr>
        <tr><td class="name">bridesmaid.example</td><td>Claritas est etiam processus dynamicus, qui sequitur mutationem.</td><td class="price">$2.99</td><td class="pay"><i class="pay-mark"></i></td></tr>
        <tr><td class="name">bronxauto.example</td><td>Lorem ipsum dolor sit amet, consectetuer adipiscing elit sed diam.</td><td class="price">$2.99</td><td class="pay"><i class="pay-mark"></i></td></tr>
        <tr><td class="name">cardealers.example</td><td>Ut wisi enim ad minim veniam, quis nostrud exerci tation.</td><td class="price">$4.99</td><td class="pay"><i class="pay-mark"></i></td></tr>
        <tr><td class="name">carforsale.example</td><td>Nam liber tempor cum soluta nobis eleifend option congue nihil.</td><td class="price">$5.99</td><td class="pay"><i class="pay-mark"></i></td></tr>
        <tr><td class="name">carforrent.example</td><td>Typi non habent claritatem insitam; est usus legentis.</td><td class="price">$6.99</td><td class="pay"><i class="pay-mark"></i></td></tr>
        <tr><td class="name">circlecenter.example</td><td>Claritas est etiam processus dynamicus, qui sequitur mutationem.</td><td class="price">$7.99</td><td class="pay"><i class="pay-mark"></i></td></tr>
        <tr><td class="name">circledash.example</td><td>Lorem ipsum dolor sit amet, consectetuer adipiscing elit sed diam.</td><td class="price">$5.99</td><td class="pay"><i class="pay-mark"></i></td></tr>
        <tr><td class="name">circlerestaurant.example</td><td>Ut wisi enim ad minim veniam, quis nostrud exerci tation.</td><td class="price">$2.99</td><td class="pay"><i class="pay-mark"></i></td></tr>
        <tr><td class="name">corelink.example</td><td>Nam liber tempor cum soluta nobis eleifend option congue nihil.</td><td class="price">$3.99</td><td class="pay"><i class="pay-mark"></i></td></tr>
        <tr><td class="name">corecorporation.example</td><td>Typi non habent claritatem insitam; est usus legentis.</td><td class="price">$2.99</td><td class="pay"><i class="pay-mark"></i></td></tr>
      </tbody>
    </table>
    <div class="scroll">
      <svg style="top:4px" width="10" height="7" viewBox="0 0 10 7"><path d="M0 7L5 0l5 7z" fill="#777"/></svg>
      <div class="thumb"></div>
      <svg style="bottom:4px" width="10" height="7" viewBox="0 0 10 7"><path d="M0 0h10L5 7z" fill="#777"/></svg>
    </div>
  </section>

  <footer class="footer">
    <div class="footer-logo">VALTRIX</div>
    <div class="about">
      <h3>ABOUT VALTRIX, INC</h3>
      <p>Lorem ipsum dolor sit amet, consectetuer adipiscing elit, sed diam nonummy nibh euismod tincidunt ut laoreet dolore magna aliquam erat volutpat. Ut wisi enim ad min im veniam, quis nostrud exerci tation ullam corper suscipit lobortis nisl ut aliquip ex ea commodo consequat. Duis autem vel eum iriure dolor in hendrerit in vulputate velit esse molestie consequat, vel illum.</p>
    </div>
    <div class="contact">
      <h3>CONTACT US</h3>
      <div class="field">Name</div>
      <div class="field">Email</div>
      <div class="field msg">Message</div>
      <span class="submit">SUBMIT</span>
    </div>
  </footer>
  <div class="copy">
    <span>COPYRIGHT © 2016 VALTRIX, INC. ALL RIGHTS RESERVED.</span>
    <span class="social"><i></i><i></i><i></i></span>
  </div>
</div>
</body>
</html>
```